Single Page/Scrolling Design for Model Recruitment site

We need a design (and if you are capable, coding) for our company, Brimwell Parlour (LA as in Los Angeles). We like modern single page designs, hence the title for the project. We have already had a designer come up with a logo, which is attached. You're free to play around with the colors, although we want the site to have a feminine appeal to it.

The site is basically a recruitment project for girls who are interested in working as chat hosts for cam sites. We don't want anything cheesy that feels like a porn site. The inspiration for the logo (and the inspiration for the site) comes from the French and English salons of the late 18th century, where beautiful and intelligent women would gather to discuss a range of topics. We want the website to convey that this work is fun and exciting. Please keep these things in mind for the design.

As I mentioned, we like the modern look and feel of single page designs, especially because we don't have a ton of content. We just need an "About us" area, a "Work from Home" area, a "Work at The Brimwell Parlour" area, and "Contact Us" area which should have text boxes for entering email, subject, a message, etc.

The logo I mentioned is attached, as well as a very crude mockup of the layout of all the content I described.

Target Market(s)

Women age 18-35.

Industry/Entity Type

It Company

Font styles to use
Serif
Decorative
Script

Colors

Designer to choose colors to be used in the design.

Requirements
Should not have
• Images that are super sexual or even slightly pornographic. We want this to appeal to a broad range of women.

```html
<!DOCTYPE html>
<html lang="en">
<head>
<meta charset="utf-8">
<title>Brimwell Parlour</title>
<link rel="stylesheet" href="https://fonts.googleapis.com/css2?family=Ubuntu:wght@400;500;700&family=Open+Sans:wght@400;600&display=swap">
<style>
  :root {
    --pink: #d9208b;
    --pink-deep: #c0167a;
    --pink-light: #e64ca3;
    --ink: #1c1c1c;
    --dark-top: #3d3d3d;
    --dark-bottom: #161616;
    --white: #ffffff;
    --grey-text: #333333;
    --pale: #f3f3f3;
  }
  * { box-sizing: border-box; margin: 0; padding: 0; }
  html, body { width: 1200px; height: 2764px; overflow: hidden; background: var(--white); }
  body { position: relative; font-family: "Open Sans", Arial, sans-serif; color: var(--grey-text); }
  .block { position: absolute; left: 0; width: 1200px; }
  .heading { font-family: "Ubuntu", Arial, sans-serif; font-weight: 500; color: var(--pink); font-size: 32px; position: absolute; }

  /* navigation */
  .site-nav { top: 0; height: 81px; background: linear-gradient(var(--dark-top), var(--dark-bottom)); }
  .site-nav a { position: absolute; top: 0; height: 81px; line-height: 81px; color: var(--white); text-decoration: none; font-family: "Ubuntu", Arial, sans-serif; font-size: 16px; font-weight: 500; text-align: center; }
  .site-nav .is-active { background: var(--pink); }

  /* welcome */
  .welcome { top: 81px; height: 476px; }
  .brand { position: absolute; left: 161px; top: 190px; width: 214px; text-align: center; }
  .brand-dot { width: 120px; height: 120px; border-radius: 50%; background: var(--pink); margin: 0 auto 18px; }
  .brand-name { font-family: "Ubuntu", Arial, sans-serif; font-weight: 500; font-size: 30px; line-height: 34px; color: var(--pink); }
  .welcome-text { position: absolute; left: 398px; top: 196px; width: 700px; font-family: "Ubuntu", Arial, sans-serif; font-size: 28px; line-height: 38px; color: #444; font-weight: 400; }
  .welcome-text strong { color: var(--ink); font-weight: 500; }

  /* about */
  .about { top: 557px; height: 468px; background: linear-gradient(#4a4a4a, var(--dark-bottom)); }
  .about .heading { left: 161px; top: 54px; }
  .about-copy { position: absolute; left: 161px; top: 104px; width: 442px; font-size: 12.6px; line-height: 18.6px; color: #e8e8e8; text-align: justify; }
  .about-photo { position: absolute; left: 603px; top: 0; width: 597px; height: 468px;
    background: radial-gradient(ellipse at 45% 55%, #d98fb0 0%, #8a6070 35%, #3d3d3d 70%, transparent 100%); }

  /* training */
  .training { top: 1025px; height: 461px; }
  .training-photo { position: absolute; left: 58px; top: 58px; width: 564px; height: 403px;
    background: radial-gradient(ellipse at 50% 50%, #c9c9cc 0%, #ebe4de 45%, #ffffff 80%); }
  .training .heading { left: 626px; top: 97px; }
  .training-copy { position: absolute; left: 633px; top: 172px; width: 383px; font-size: 12.6px; line-height: 18.4px; color: var(--grey-text); text-align: justify; }

  /* work from home */
  .home-work { top: 1486px; height: 322px; background: linear-gradient(160deg, var(--pink-light), var(--pink) 45%, var(--pink-deep)); }
  .home-work .heading { color: var(--white); left: 230px; top: 78px; }
  .home-work-copy { position: absolute; left: 230px; top: 130px; width: 610px; font-family: "Ubuntu", Arial, sans-serif; font-size: 21px; line-height: 27px; color: #fbe3f0; }

  /* call to action */
  .actions { top: 1808px; height: 242px; background: linear-gradient(#3c3c3c, var(--dark-bottom)); }
  .action-button { position: absolute; top: 44px; width: 370px; height: 147px; line-height: 147px; text-align: center;
    background: linear-gradient(var(--pink-light), var(--pink) 50%, var(--pink-deep));
    color: var(--white); font-family: "Ubuntu", Arial, sans-serif; font-size: 26px; font-weight: 500; text-decoration: none;
    box-shadow: 0 8px 10px rgba(0,0,0,.55); }

  /* contact */
  .contact { top: 2050px; height: 663px; }
  .contact .heading { left: 161px; top: 92px; }
  .contact-photo { position: absolute; left: 184px; top: 173px; width: 346px; height: 414px;
    background: radial-gradient(ellipse at 50% 55%, #d8d2cc 0%, #eeeae6 50%, #ffffff 85%); }
  .contact-form { position: absolute; left: 564px; top: 154px; width: 454px; height: 364px; background: var(--pink); border-radius: 4px; }
  .field { position: absolute; left: 23px; width: 327px; height: 42px; background: var(--white); border: 0; border-radius: 4px;
    font-family: "Open Sans", Arial, sans-serif; font-size: 12px; color: var(--pink); padding: 12px 10px; }
  .field-message { width: 408px; height: 198px; resize: none; }
  .send-button { position: absolute; left: 871px; top: 543px; width: 142px; height: 49px; border: 0;
    background: linear-gradient(var(--pink-light), var(--pink-deep)); color: var(--white);
    font-family: "Ubuntu", Arial, sans-serif; font-size: 19px; font-weight: 500; }

  /* footer */
  .site-footer { top: 2713px; height: 51px; background: #1e1e1e; }
  .to-top { position: absolute; left: 1027px; top: 0; height: 51px; line-height: 51px; color: var(--pink); font-family: "Ubuntu", Arial, sans-serif; font-size: 19px; text-decoration: none; }
  .to-top svg { vertical-align: -1px; margin-left: 6px; }
</style>
</head>
<body>

<nav class="block site-nav">
  <a href="#about" style="left:230px;width:80px;">About Us</a>
  <a href="#training" class="is-active" style="left:378px;width:225px;font-size:14px;">Train @ The Brimwell Parlour</a>
  <a href="#home-work" style="left:667px;width:140px;">Work from home</a>
  <a href="#contact" style="left:888px;width:80px;">Contact</a>
</nav>

<header class="block welcome">
  <div class="brand">
    <div class="brand-dot"></div>
    <div class="brand-name">Brimwell Parlour</div>
  </div>
  <p class="welcome-text"><strong>Welcome to the Brimwell Parlour</strong>, a unique portal into the world of webcam modeling and chat hosting</p>
</header>

<section class="block about" id="about">
  <h2 class="heading">About Us</h2>
  <p class="about-copy">Brimwell Parlour takes its spirit from the salons of the late eighteenth century, where bright and curious women gathered to talk about art, books, travel and the news of the day. We bring that same warmth online. Our hosts lead friendly, clever conversation from the comfort of home, set their own hours and join a supportive team that values wit as much as charm. We offer training, steady guidance and a safe, respectful place to grow. Whether you are a student, a parent or simply someone who loves to talk, there is a seat waiting for you in our parlour.</p>
  <div class="about-photo" role="img" aria-label="Photo of a smiling young woman in a pink top holding an open laptop"></div>
</section>

<section class="block training" id="training">
  <div class="training-photo" role="img" aria-label="Photo of a hand holding a silver webcam"></div>
  <h2 class="heading">Tran @ Brimwell Parlour</h2>
  <p class="training-copy">New hosts start with a relaxed training course that covers chat etiquette, lighting, camera setup and how to keep a conversation lively. Our coaches walk you through every step, answer questions along the way and help you build confidence before your first session. You will learn at your own pace with a friendly team beside you.</p>
</section>

<section class="block home-work" id="home-work">
  <h2 class="heading">Work From Home</h2>
  <p class="home-work-copy">Working as an webcam entertainer can be very lucrative business, wheter it is your only job or something you do on the side. It gives you the flexibility to create your own schedule based around your availability</p>
</section>

<section class="block actions">
  <a href="#contact" class="action-button" style="left:223px;">What do I need?</a>
  <a href="#contact" class="action-button" style="left:624px;">How do I sign Up</a>
</section>

<section class="block contact" id="contact">
  <h2 class="heading">Contact Us</h2>
  <div class="contact-photo" role="img" aria-label="Photo of a blonde woman sitting cross-legged with a laptop"></div>
  <form class="contact-form">
    <input class="field" style="top:30px;" type="text" placeholder="Name" aria-label="Name">
    <input class="field" style="top:86px;" type="email" placeholder="Email address" aria-label="Email address">
    <textarea class="field field-message" style="top:143px;" placeholder="Message" aria-label="Message"></textarea>
  </form>
  <button class="send-button" type="button">Send</button>
</section>

<footer class="block site-footer">
  <a href="#" class="to-top">Up<svg width="20" height="18" viewBox="0 0 20 18" aria-hidden="true"><path d="M10 1 L19 17 L1 17 Z" fill="#d9208b"/></svg></a>
</footer>

</body>
</html>
```